Exhibition Stand Design for innovative Social Business

We are an innovative social business empowering people to value nature through KEV, a complementary digital currency. We have attached the MY_KEV branding document, and are needing a design for our exhibition stand (https://salonvorta.example/produit/stand-parapluie-classic-pvc-3x4c/. The attached doc mocks up a stand on page 32, though we would like some messaging included, in line with our website www.mykev.example. You will see there how the branding concept has been implemented with the OUR:ROOTS, COINS, EARTH wording, as well as All gain together. Our green colours are included in the branding document. Many thanks!

Industry/Entity Type

Environment

Font styles to use
Other font styles liked:
• As per our attached fonts

Requirements
Must have
• Our attached branding guidelines gives our look and feel - Innovative / Dynamic / Vibrant / Reliable / Accessible / Connected.

```html
<!DOCTYPE html>
<html lang="en">
<head>
<meta charset="utf-8">
<title>KEV Exhibition Stand</title>
<link rel="stylesheet" href="https://fonts.googleapis.com/css2?family=Lexend:wght@400;500;600;700&display=swap">
<style>
  :root {
    --page-bg: #e9e9e9;
    --green-teal: #45d99a;
    --green-mid: #4be48a;
    --green-bright: #22e23c;
    --ink: #141414;
    --white: #ffffff;
    --bubble: rgba(255, 255, 255, 0.16);
  }
  * { margin: 0; padding: 0; box-sizing: border-box; }
  html, body { width: 1200px; height: 960px; overflow: hidden; }
  body {
    background: var(--page-bg);
    font-family: "Lexend", "Helvetica Neue", Arial, sans-serif;
    position: relative;
  }
  .backwall, .counter {
    position: absolute;
    overflow: hidden;
    background: linear-gradient(90deg, var(--green-teal) 0%, var(--green-mid) 50%, var(--green-bright) 100%);
  }
  .backwall { left: 40px; top: 200px; width: 760px; height: 525px; }
  .counter  { left: 850px; top: 330px; width: 310px; height: 340px;
    background: linear-gradient(180deg, var(--green-mid) 0%, var(--green-teal) 100%); }
  .bubble { position: absolute; border-radius: 50%; background: var(--bubble); }
  .brand-name {
    position: absolute;
    font-weight: 600;
    color: var(--ink);
    letter-spacing: 2px;
    line-height: 1;
  }
  .backwall .brand-name { left: 146px; top: 66px; font-size: 88px; }
  .pillars { position: absolute; left: 148px; top: 172px; font-weight: 600; line-height: 51px; font-size: 46px; }
  .pillars .lead { color: var(--ink); }
  .pillars .word { color: var(--white); }
  .tagline { position: absolute; font-weight: 400; color: var(--ink); white-space: nowrap; }
  .tagline strong { font-weight: 500; color: var(--white); }
  .backwall .tagline { left: 412px; top: 282px; font-size: 30px; }
  .counter .brand-name { left: 0; right: 0; text-align: center; top: 56px; font-size: 54px; }
  .counter .tagline { left: 0; right: 0; text-align: center; top: 170px; font-size: 28px; }
  .web-address {
    position: absolute; left: 0; right: 0; top: 272px; text-align: center;
    font-size: 16px; font-weight: 500; color: var(--ink);
  }
</style>
</head>
<body>
  <section class="backwall" aria-label="Backwall graphic">
    <div class="bubble" style="left:525px;top:8px;width:232px;height:232px;"></div>
    <div class="bubble" style="left:357px;top:184px;width:284px;height:284px;"></div>
    <div class="bubble" style="left:0px;top:319px;width:224px;height:224px;"></div>
    <div class="brand-name">KEV</div>
    <div class="pillars">
      <div class="lead">OUR:</div>
      <div class="word">ROOTS</div>
      <div class="word">COINS</div>
      <div class="word">EARTH</div>
    </div>
    <p class="tagline">All gain <strong>TOGETHER</strong></p>
  </section>

  <section class="counter" aria-label="Counter graphic">
    <div class="bubble" style="left:130px;top:120px;width:240px;height:240px;"></div>
    <div class="bubble" style="left:-60px;top:150px;width:200px;height:200px;"></div>
    <div class="brand-name">KEV</div>
    <p class="tagline">All gain <strong>TOGETHER</strong></p>
    <p class="web-address">www.mykev.example</p>
  </section>
</body>
</html>
```